Health Coaching Flyer for New Clients

I need a two-sided flyer (3.5" x 8.5" preferred or 5" x 7") to distribute to potential coaching clients. My business name is Talvora Health & Wellness Coaching. My business is focused on helping people with habit changes that contribute to their overall well-being. I would like the design colors to be gender neutral. I would like a small photo of myself near the "my name is Jen" statement. Please feel free to change the logo color to match the design.

Target Market(s)

Adults of all ages.

Font styles to use
Serif

Requirements
Must have
• Emphasize my opening question (found in health coaching brochure - attached).
• Small picture of myself near "my name is Jen" statement.
Should not have
• No light of pastel colors.

```html
<!DOCTYPE html>
<html lang="en">
<head>
<meta charset="utf-8">
<title>Talvora Health &amp; Wellness Coaching – Flyer</title>
<link rel="stylesheet" href="https://fonts.googleapis.com/css2?family=Montserrat:wght@600;700;800&family=Arimo:wght@400;700&display=swap">
<style>
  :root {
    --brand-blue: #1a86c4;
    --brand-blue-deep: #1570a8;
    --ink: #222629;
    --muted-grey: #8c8f92;
    --sheen-grey: #e4e6e8;
    --paper: #ffffff;
    --stage: #e2ddd7;
    --photo-warm: #d9cbbd;
    --photo-cool: #c9d4dc;
    --pill-light: #bcd9ee;
  }
  * { box-sizing: border-box; margin: 0; padding: 0; }
  html, body { width: 1200px; height: 900px; overflow: hidden; }
  body {
    background: var(--stage);
    font-family: "Arimo", Arial, sans-serif;
    color: var(--ink);
    position: relative;
  }
  .flyer {
    position: absolute;
    top: 30px;
    width: 347px;
    height: 840px;
    background: var(--paper);
    overflow: hidden;
    box-shadow: 0 4px 14px rgba(0,0,0,.18);
  }
  .flyer--front { left: 223px; background: linear-gradient(160deg, #fff 18%, var(--sheen-grey) 38%, #fff 62%, #fff 100%); }
  .flyer--back { left: 630px; }
  .abs { position: absolute; }
  .heading { font-family: "Montserrat", Arial, sans-serif; color: var(--brand-blue); font-weight: 800; }
  .placeholder { position: absolute; }

  /* front */
  .front-title { left: 0; width: 347px; top: 60px; text-align: center; font-size: 35px; letter-spacing: 4px; padding-left: 28px; }
  .front-subtitle { left: 0; width: 347px; top: 103px; text-align: center; font-size: 18px; letter-spacing: 4px; color: var(--ink); font-family: "Arimo", sans-serif; padding-left: 28px; }
  .couple-photo {
    left: 143px; top: 199px; width: 210px; height: 210px; border-radius: 50%;
    background: radial-gradient(circle at 45% 45%, var(--photo-warm), #b9a99a 70%, #dfe6ea);
    border: 4px solid var(--brand-blue);
  }
  .heart-ornament { background: radial-gradient(ellipse at center, rgba(26,134,196,.28), rgba(26,134,196,.05) 70%); border-radius: 40%; }
  .front-heart-text { left: 42px; top: 224px; width: 90px; text-align: center; font-family: "Montserrat", sans-serif; font-weight: 700; font-size: 13px; line-height: 14px; letter-spacing: 1px; color: var(--ink); }
  .wordmark { font-family: "Montserrat", sans-serif; font-weight: 800; letter-spacing: 2px; color: var(--brand-blue); }
  .front-wordmark { left: 21px; top: 458px; font-size: 22px; }
  .opening-question { left: 19px; top: 530px; width: 315px; font-size: 12.6px; line-height: 16px; letter-spacing: 1px; font-weight: 700; }
  .intro-copy { left: 19px; top: 574px; width: 308px; font-size: 9.4px; line-height: 13.3px; letter-spacing: .9px; text-align: justify; }
  .headshot {
    width: 104px; height: 104px; border-radius: 50%;
    background: radial-gradient(circle at 50% 40%, #d8b8a2, #6b4e3f 75%);
    border: 3px solid var(--brand-blue);
  }
  .front-headshot { left: 0; top: 691px; }
  .swoosh { position: absolute; left: 0; top: 0; }
  .front-contact { right: 0; width: 230px; top: 770px; text-align: center; color: #fff; padding-left: 20px; }
  .front-contact .label { font-family: "Montserrat", sans-serif; font-weight: 700; font-size: 13.5px; letter-spacing: 2px; margin-bottom: 6px; }
  .front-contact p { font-size: 9px; letter-spacing: 1px; line-height: 11px; }

  /* back */
  .back-wordmark { right: 12px; top: 26px; font-size: 15px; }
  .back-heart-text { left: 28px; top: 126px; font-family: "Montserrat", sans-serif; color: var(--brand-blue); font-weight: 700; font-size: 13px; letter-spacing: 2px; line-height: 13px; }
  .back-heart-text span { display: block; font-size: 7.5px; color: var(--ink); font-weight: 600; letter-spacing: 1px; }
  .back-service-name { left: 120px; width: 210px; top: 255px; text-align: center; font-size: 16px; line-height: 18px; letter-spacing: 1.5px; font-weight: 700; }
  .section-title { left: 18px; top: 327px; font-size: 12.6px; letter-spacing: 1.4px; font-weight: 700; }
  .benefit-list { left: 24px; top: 353px; width: 310px; list-style: none; }
  .benefit-list li { position: relative; padding-left: 20px; font-size: 8px; line-height: 11px; letter-spacing: .9px; color: var(--brand-blue); margin-bottom: 7px; }
  .benefit-list svg { position: absolute; left: 0; top: 1px; }
  .invite-box { left: 18px; top: 539px; width: 310px; border-top: 1.5px dashed var(--brand-blue); border-bottom: 1.5px dashed var(--brand-blue); padding: 6px 10px 7px; font-size: 9.2px; line-height: 13.4px; letter-spacing: .9px; }
  .offer-title { left: 0; width: 347px; top: 623px; text-align: center; font-size: 25px; letter-spacing: 2px; }
  .offer-arrow { left: 30px; top: 658px; }
  .offer-copy { left: 84px; top: 660px; width: 245px; font-size: 9.2px; line-height: 13.4px; letter-spacing: 1px; text-align: justify; }
  .ready-pill { left: 18px; top: 720px; width: 238px; height: 30px; border-radius: 8px; background: linear-gradient(90deg, var(--pill-light), #e6f1f9); font-size: 8.6px; line-height: 12px; letter-spacing: .9px; text-align: center; padding-top: 3px; font-weight: 700; color: #2b4457; }
  .back-contact-label { left: 13px; top: 775px; font-size: 13.5px; letter-spacing: 2px; font-weight: 700; }
  .name-tag { left: 142px; top: 775px; padding: 2px 8px; border: 1.5px dashed var(--brand-blue); font-size: 8.6px; letter-spacing: 1px; color: var(--brand-blue); }
  .back-details { left: 13px; top: 803px; font-size: 8.6px; letter-spacing: 1px; word-spacing: 3px; }
  .back-details span + span { margin-left: 22px; }
  .back-headshot { left: 249px; top: 729px; }
</style>
</head>
<body>

<section class="flyer flyer--front" aria-label="Flyer front">
  <h1 class="abs heading front-title">IMPROVE</h1>
  <p class="abs front-subtitle">YOUR HEALTH</p>

  <div class="placeholder heart-ornament" style="left:8px;top:170px;width:155px;height:151px" role="img" aria-label="Large blue swirl heart ornament"></div>
  <p class="abs front-heart-text">HEALTH &amp;<br>Wellness<br>Coaching</p>
  <div class="placeholder heart-ornament" style="left:91px;top:363px;width:59px;height:56px" role="img" aria-label="Medium blue heart ornament"></div>
  <div class="placeholder heart-ornament" style="left:94px;top:417px;width:34px;height:32px" role="img" aria-label="Small blue heart ornament"></div>

  <div class="placeholder couple-photo" role="img" aria-label="Photo of a smiling young couple embracing"></div>

  <p class="abs wordmark front-wordmark">TALVORA</p>

  <h2 class="abs heading opening-question">Need support in making real, lasting lifestyle and behavior changes?</h2>
  <p class="abs intro-copy">My name is Jen. &nbsp;I am studying to become an KINDRA-Certified Functional Health Coach. &nbsp;My training involves many science-based practices that improve both our health and how we grow and change as humans. &nbsp;I now have the opportunity to turn that knowledge into practice by coaching actual clients interested in improving their own health and well-being.</p>

  <svg class="swoosh" width="347" height="840" viewBox="0 0 347 840" aria-hidden="true">
    <path d="M0 840 L0 800 Q90 722 347 712 L347 840 Z" fill="#b8bcc0"/>
    <path d="M18 840 Q120 748 347 735 L347 840 Z" fill="var(--brand-blue)"/>
  </svg>
  <div class="placeholder headshot front-headshot" role="img" aria-label="Small portrait photo of Jen"></div>

  <div class="abs front-contact">
    <p class="label">CONTACT US</p>
    <p>Jen Talvora</p>
    <p>555-014-2290</p>
    <p>talvorahwc@mailbox.net</p>
  </div>
</section>

<section class="flyer flyer--back" aria-label="Flyer back">
  <svg class="swoosh" width="347" height="240" viewBox="0 0 347 240">
    <defs>
      <linearGradient id="seniorsPhotoTone" x1="0" y1="0" x2="1" y2="1">
        <stop offset="0" stop-color="#d6cdc4"/>
        <stop offset=".55" stop-color="#e8d9d3"/>
        <stop offset="1" stop-color="#cfd6dc"/>
      </linearGradient>
    </defs>
    <path d="M0 0 H347 V125 Q200 188 0 198 Z" fill="url(#seniorsPhotoTone)" role="img" aria-label="Photo of a smiling senior couple"/>
    <path d="M0 198 Q200 188 347 125 Q230 205 0 222 Z" fill="var(--brand-blue)"/>
  </svg>
  <p class="abs wordmark back-wordmark" style="color:var(--muted-grey)">TALVORA</p>
  <div class="placeholder heart-ornament" style="left:10px;top:90px;width:130px;height:110px" role="img" aria-label="Blue swirl heart ornament"></div>
  <p class="abs back-heart-text">IMPROVE<span>YOUR HEALTH</span></p>

  <div class="placeholder heart-ornament" style="left:52px;top:220px;width:52px;height:55px" role="img" aria-label="Blue heart ornament"></div>
  <div class="placeholder heart-ornament" style="left:67px;top:279px;width:27px;height:25px" role="img" aria-label="Small blue heart ornament"></div>
  <h2 class="abs heading back-service-name">HEALTH &amp; Wellness<br>Coaching</h2>

  <h3 class="abs heading section-title">Functional health coaches</h3>
  <ul class="abs benefit-list">
    <li><svg width="12" height="11" viewBox="0 0 12 11"><path d="M6 10 C2 7 1 5 1 3.4 A2.4 2.4 0 0 1 6 2.6 A2.4 2.4 0 0 1 11 3.4 C11 5 10 7 6 10Z" fill="none" stroke="#1a86c4" stroke-width="1.3"/></svg>Leverage your strengths rather than focus on your weaknesses</li>
    <li><svg width="12" height="11" viewBox="0 0 12 11"><path d="M6 10 C2 7 1 5 1 3.4 A2.4 2.4 0 0 1 6 2.6 A2.4 2.4 0 0 1 11 3.4 C11 5 10 7 6 10Z" fill="none" stroke="#1a86c4" stroke-width="1.3"/></svg>Support you in finding your own strategies and motivation for change</li>
    <li><svg width="12" height="11" viewBox="0 0 12 11"><path d="M6 10 C2 7 1 5 1 3.4 A2.4 2.4 0 0 1 6 2.6 A2.4 2.4 0 0 1 11 3.4 C11 5 10 7 6 10Z" fill="none" stroke="#1a86c4" stroke-width="1.3"/></svg>Provide a judgment-free zone and support your autonomy</li>
    <li><svg width="12" height="11" viewBox="0 0 12 11"><path d="M6 10 C2 7 1 5 1 3.4 A2.4 2.4 0 0 1 6 2.6 A2.4 2.4 0 0 1 11 3.4 C11 5 10 7 6 10Z" fill="none" stroke="#1a86c4" stroke-width="1.3"/></svg>Use an experimental mindset to find and develop sustainable habits</li>
    <li><svg width="12" height="11" viewBox="0 0 12 11"><path d="M6 10 C2 7 1 5 1 3.4 A2.4 2.4 0 0 1 6 2.6 A2.4 2.4 0 0 1 11 3.4 C11 5 10 7 6 10Z" fill="none" stroke="#1a86c4" stroke-width="1.3"/></svg>Act as your accountability partner as you reach your unique health goals; whether they be improving sleep, diet, fitness, social connection, or reducing stress.</li>
  </ul>

  <p class="abs invite-box">I would like to invite you to participate with me as a client as I continue to hone my coaching skills. We can develop a plan and schedule that aligns with your goals.</p>

  <h2 class="abs heading offer-title">Limited Time Offer</h2>
  <svg class="abs offer-arrow" width="48" height="36" viewBox="0 0 48 36" aria-hidden="true">
    <path d="M3 34 C5 18 16 12 30 12 L30 4 L46 16 L30 29 L30 21 C19 21 10 25 3 34 Z" fill="var(--brand-blue)"/>
  </svg>
  <p class="abs offer-copy">As a way to give back to my community, I am offering new clients six free coaching sessions.</p>

  <p class="abs ready-pill">I'm ready to support you as you work<br>to improve your health.</p>

  <p class="abs heading back-contact-label">CONTACT US</p>
  <p class="abs name-tag">Jen Talvora</p>
  <p class="abs back-details"><span>555-014-2290</span><span>talvorahwc@mailbox.net</span></p>

  <div class="placeholder headshot back-headshot" role="img" aria-label="Small portrait photo of Jen"></div>
</section>

</body>
</html>
```